Business Card and Stationary for Commercial Real Estate Brokerage
Tarvel Commercial
Business Card and Stationary for Commercial Real Estate Brokerage - Real Estate
Creative Brief
Use specific fonts
Use same as logo font or other, whichever looks best
Professional
Dorian P. Lusk
Senior Vice President
4821 Halbrook Avenue, Newport Beach, CA 92660
dlusk@tarvelpx.example
www.tarvelpx.example
CA DRE: 04263918
Please include additional business location with the following address and contact information in no particular order, as a placeholder: 318 Quillan Avenue, New York, NY 10166 Phone: 347-555-0192 License No. NY DRE: 86420913

```html
<!DOCTYPE html>
<html lang="en">
<head>
<meta charset="utf-8">
<title>Tarvel Commercial – Business Card</title>
<link href="https://fonts.googleapis.com/css2?family=Roboto:wght@300;400;500;700;900&display=swap" rel="stylesheet">
<style>
  :root {
    --page-bg: #e9e9ec;
    --card-white: #ffffff;
    --brand-navy: #1f2c80;
    --brand-blue: #3246a8;
    --brand-deep: #141d5e;
    --tagline-grey: #8a93b8;
    --text-blue: #1f2f86;
    --divider: #3a4aa0;
  }
  * { box-sizing: border-box; margin: 0; padding: 0; }
  html, body {
    width: 1200px; height: 901px; overflow: hidden;
    background: var(--page-bg);
    font-family: "Roboto", Arial, sans-serif;
  }
  .stage { position: relative; width: 1200px; height: 901px; }
  .card {
    position: absolute; left: 240px; width: 720px; height: 411px;
    border-radius: 4px; overflow: hidden;
    box-shadow: 0 6px 18px rgba(0,0,0,0.18);
  }
  /* Front */
  .card-front { top: 28px; background: var(--card-white); }
  .brand { position: absolute; left: 0; right: 0; top: 48px; text-align: center; }
  .brand-name {
    font-weight: 900; font-size: 50px; letter-spacing: 3px;
    color: var(--brand-navy); text-transform: uppercase; line-height: 1;
  }
  .brand-tagline {
    margin-top: 10px; font-weight: 300; font-size: 15px;
    letter-spacing: 9px; color: var(--tagline-grey); text-transform: uppercase;
  }
  .name-band {
    position: absolute; left: 0; right: 0; top: 170px; height: 68px;
    background: linear-gradient(90deg, var(--brand-deep), var(--brand-blue) 50%, var(--brand-deep));
    color: #fff; text-align: center; padding-top: 8px;
  }
  .person-name { font-weight: 700; font-size: 28px; line-height: 1.1; }
  .person-title { font-weight: 400; font-size: 15px; margin-top: 3px; opacity: .92; }
  .contact {
    position: absolute; left: 36px; right: 36px; top: 254px;
    color: var(--text-blue); font-size: 16px; line-height: 1.45; text-align: center;
  }
  .contact strong { font-weight: 700; }
  .sep { color: var(--divider); margin: 0 8px; }
  .offices { display: flex; justify-content: center; margin-top: 10px; }
  .office { padding: 0 22px; text-align: left; font-size: 16px; }
  .office + .office { border-left: 2px solid var(--divider); }
  .front-rule {
    position: absolute; left: 0; right: 0; bottom: 0; height: 10px;
    background: var(--brand-navy);
  }
  /* Back */
  .card-back {
    top: 462px;
    background: radial-gradient(ellipse at 50% 45%, var(--brand-blue), var(--brand-deep) 80%);
    color: #fff;
  }
  .card-back .brand { top: 140px; }
  .card-back .brand-name { color: #ffffff; font-size: 56px; }
  .card-back .brand-tagline { color: #c3cbee; }
  .back-web {
    position: absolute; left: 0; right: 0; bottom: 70px; text-align: center;
    font-size: 15px; color: #dfe4fb; letter-spacing: .5px;
  }
</style>
</head>
<body>
<div class="stage">
  <section class="card card-front" aria-label="Business card front">
    <div class="brand">
      <div class="brand-name">Tarvel Commercial</div>
      <div class="brand-tagline">Real Estate Services</div>
    </div>
    <div class="name-band">
      <div class="person-name">Dorian P. Lusk</div>
      <div class="person-title">Senior Vice President</div>
    </div>
    <div class="contact">
      <div><strong>Phone/Fax:</strong> 949-555-0186 (CA) / 347-555-0192 (NY)<span class="sep">|</span><strong>Mobile:</strong> 949-555-0147</div>
      <div><strong>Email:</strong> dlusk@tarvelpx.example<span class="sep">|</span><strong>Website:</strong> www.tarvelpx.example</div>
      <div class="offices">
        <div class="office">4821 Halbrook Avenue,<br>Harborview, CA 92698</div>
        <div class="office">318 Quillan Avenue,<br>Eastbrook, NY 10199</div>
      </div>
    </div>
    <div class="front-rule"></div>
  </section>

  <section class="card card-back" aria-label="Business card back">
    <div class="brand">
      <div class="brand-name">Tarvel Commercial</div>
      <div class="brand-tagline">Real Estate Services</div>
    </div>
    <div class="back-web">www.tarvelpx.example</div>
  </section>
</div>
</body>
</html>
```